On-the-go, individually packaged flushable wipe packaging

Design the front and back of an individually packaged flushable wipe product.

The package is 4 inches tall and 2 inches wide. There are only two sides to the package, front and back. It is constructed of two sheets of printed, foil-lined plastic that are heat welded together.

The front should be decorative and playful and have space for a logo / product name on it (no logo has been created yet so use your imagination if you wish). It should be unisex and envoke somewhat outdoorsy vibes that would appeal to mountain bikers, marathon runners, travelers, and adventurers of all kinds. It can draw attention to itself through color but not through potty humor or bathroom references. People should be able to take these to work or send them with their children to school with being embarrassed.

Important note: Similar to business cards, the packaging material is printed and then cut in a grid. The machine that cuts the packaging may be off by a couple millimeters so any artwork or colors that extend to the sides of the packaging should continue onto the opposite side of the next package like a tesselation or book-matched wood, left side should match up to right side and top should match up to bottom.

The back should contain the follow information (iconography and layout up to you):

- Contains one hygienic towelette
- (Key selling points)
- Flushable & Biodegradable
- 100% natural fibers
- Gentle cleansing formula
- No parabens or fragrances
- (For use on…)
- Hands
- Face*
- Body
- Nether areas
- Messy surfaces
- *Avoid eyes/forehead before sweating and scruff (snags fibers)
- Please care for our planet, cities, and sewer systems by recycling this packaging after use. Do not flush packaging.

```html
<!DOCTYPE html>
<html lang="en">
<head>
<meta charset="utf-8">
<title>Trail Breeze flushable wipes – front and back</title>
<link href="https://fonts.googleapis.com/css2?family=Exo+2:wght@300;400;600;700;800&display=swap" rel="stylesheet">
<style>
  :root{
    --backdrop:#bcc2a8;
    --pouch:#f4f4f4;
    --pouch-edge:#e3e3e3;
    --navy:#1f3f9c;
    --sky:#1e7fd0;
    --meadow:#3fae45;
    --lime:#9cd04a;
    --orange:#f29a2e;
    --orange-deep:#e0701c;
    --ink:#161616;
    --white:#ffffff;
  }
  *{box-sizing:border-box;margin:0;padding:0}
  html,body{width:1200px;height:952px;overflow:hidden}
  body{background:var(--backdrop);font-family:"Exo 2",sans-serif;position:relative}

  .packet{position:absolute;top:74px;width:402px;height:804px;background:var(--pouch);
    border:16px solid var(--pouch-edge);border-radius:2px}
  .packet--front{left:166px}
  .packet--back{left:633px}
  .packet > *{position:absolute}
  .packet{padding:0}
  .layer{position:absolute;left:-16px;top:-16px;width:402px;height:804px}
  .layer > *{position:absolute}

  .artwork{left:38px;top:58px;width:325px;height:651px;border-radius:163px/230px;
    background:linear-gradient(180deg,var(--navy) 0%,#2459b8 25%,var(--sky) 45%,#2f6fc0 58%,var(--meadow) 72%,#2e8e4a 88%,#214f9a 100%)}
  .logo-notch{left:126px;top:-20px;width:150px;height:150px;border-radius:50%;background:var(--pouch)}
  .brand{left:0;width:402px;top:24px;text-align:center;color:#2a2a2a}
  .brand-dot{display:block;width:38px;height:38px;border-radius:50%;background:var(--orange-deep);margin:0 auto 10px}
  .brand-name{font-weight:700;font-size:19px;line-height:20px}

  .centered{left:0;width:402px;text-align:center;color:var(--white)}
  .kicker{font-weight:300;font-size:28px;line-height:28px}
  .title{font-weight:800;font-size:82px;line-height:70px;letter-spacing:1px}
  .title--inline{font-size:46px;line-height:46px;letter-spacing:0}
  .subtitle{font-weight:400;font-size:30px;line-height:30px}

  .feature{display:flex;align-items:center;gap:10px;color:var(--white);font-weight:700;font-size:17px;line-height:20px;letter-spacing:.3px}
  .feature-icon{width:42px;height:42px;border-radius:50%;background:var(--orange);flex:none;display:flex;align-items:center;justify-content:center}
  .feature-icon svg{width:24px;height:24px}

  .seal{left:265px;top:605px;width:100px;height:100px;border-radius:50%;background:var(--orange);border:4px solid var(--white);box-shadow:inset 0 0 0 6px var(--orange),inset 0 0 0 8px var(--white)}

  .size-box{left:38px;top:699px;width:73px;height:73px;background:var(--ink);border-radius:6px;color:var(--white);
    font-weight:700;font-size:18px;line-height:19px;text-align:center;padding-top:9px}
  .size-box .times{color:var(--orange)}
  .free-list{left:121px;top:724px;font-weight:700;font-size:19px;line-height:24px;color:var(--ink)}
  .free-list .accent{color:var(--orange)}

  .rule{height:1px;background:rgba(255,255,255,.7);left:67px;width:268px}
  .uses{font-weight:300;font-size:28px;line-height:33.5px}
  .mini-feature{display:flex;align-items:center;gap:6px;color:var(--white);font-weight:700;font-size:11.5px;line-height:13px;text-align:center}
  .mini-feature .feature-icon{width:27px;height:27px}
  .mini-feature .feature-icon svg{width:16px;height:16px}
  .footnote{left:67px;width:275px;color:var(--white);font-weight:300;font-size:12.6px;line-height:16px}
  .care{font-weight:400;font-size:16px;line-height:20px}
  .care strong{font-weight:700}
</style>
</head>
<body>

<svg width="0" height="0" style="position:absolute">
  <defs>
    <symbol id="icon-towel" viewBox="0 0 24 24"><rect x="3" y="7" width="18" height="10" rx="3" fill="none" stroke="#161616" stroke-width="2"/><path d="M3 12h18" stroke="#161616" stroke-width="2"/></symbol>
    <symbol id="icon-swirl" viewBox="0 0 24 24"><path d="M12 12m-2 0a2 2 0 1 0 4 0a4 4 0 1 0-8 0a6 6 0 1 0 12 0" fill="none" stroke="#161616" stroke-width="2.4" stroke-linecap="round"/></symbol>
    <symbol id="icon-leaf" viewBox="0 0 24 24"><path d="M5 19C5 10 11 5 20 4c0 9-5 15-14 15z" fill="none" stroke="#161616" stroke-width="2"/><path d="M5 19L14 10" stroke="#161616" stroke-width="2"/></symbol>
    <symbol id="icon-heart" viewBox="0 0 24 24"><path d="M12 15s-6-3.5-6-7.5A3 3 0 0 1 12 6a3 3 0 0 1 6 1.5C18 11.5 12 15 12 15z" fill="#161616"/><path d="M3 17h5l4 3h7" fill="none" stroke="#161616" stroke-width="2" stroke-linecap="round"/></symbol>
  </defs>
</svg>

<!-- Front -->
<section class="packet packet--front">
  <div class="layer">
    <div class="artwork" role="img" aria-label="Illustrated landscape of blue mountain ridges over rolling green hills with trees"></div>
    <div class="logo-notch"></div>
    <div class="brand"><span class="brand-dot"></span><span class="brand-name">Ridgeline Basics</span></div>

    <p class="centered kicker" style="top:159px">ON-THE-GO</p>
    <h1 class="centered title" style="top:197px">TRAIL<br>BREEZE</h1>
    <p class="centered subtitle" style="top:343px">flushable wipes</p>

    <div class="feature" style="left:92px;top:395px"><span class="feature-icon"><svg><use href="#icon-towel"/></svg></span>1PC HYGIENIC<br>TOWELETTE</div>
    <div class="feature" style="left:92px;top:455px"><span class="feature-icon"><svg><use href="#icon-swirl"/></svg></span>FLUSHABLE &amp;<br>BIODEGRADABLE</div>
    <div class="feature" style="left:92px;top:515px"><span class="feature-icon"><svg><use href="#icon-leaf"/></svg></span>100% NATURAL<br>FIBERS</div>
    <div class="feature" style="left:92px;top:575px"><span class="feature-icon"><svg><use href="#icon-heart"/></svg></span>GENTLE CLEANSING<br>FORMULA</div>

    <div class="seal" aria-hidden="true"></div>

    <div class="size-box">10CM<br><span class="times">X</span><br>12CM</div>
    <p class="free-list">FRAGRANCES <span class="accent">FREE</span><br>PARABENS <span class="accent">FREE</span></p>
  </div>
</section>

<!-- Back -->
<section class="packet packet--back">
  <div class="layer">
    <div class="artwork" role="img" aria-label="Illustrated landscape of blue mountain ridges over rolling green hills with trees"></div>
    <div class="logo-notch"></div>
    <div class="brand"><span class="brand-dot"></span><span class="brand-name">Ridgeline Basics</span></div>

    <p class="centered kicker" style="top:146px">ON-THE-GO</p>
    <h2 class="centered title title--inline" style="top:177px">TRAIL BREEZE</h2>
    <p class="centered subtitle" style="top:226px;font-size:28px">flushable wipes</p>
    <div class="rule" style="top:271px"></div>

    <p class="centered uses" style="top:286px">FOR USE ON: HANDS,<br>FACE*, BODY, NETHER<br>AREAS, MESSY<br>SURFACES</p>
    <div class="rule" style="top:427px"></div>

    <div class="mini-feature" style="left:66px;top:446px"><span class="feature-icon"><svg><use href="#icon-towel"/></svg></span>1PC HYGIENIC<br>TOWELETTE</div>
    <div class="mini-feature" style="left:199px;top:446px"><span class="feature-icon"><svg><use href="#icon-leaf"/></svg></span>100% NATURAL<br>FIBERS</div>
    <div class="mini-feature" style="left:66px;top:485px"><span class="feature-icon"><svg><use href="#icon-swirl"/></svg></span>FLUSHABLE &amp;<br>BIODEGRADABLE</div>
    <div class="mini-feature" style="left:199px;top:485px"><span class="feature-icon"><svg><use href="#icon-heart"/></svg></span>GENTLE CLEANSING<br>FORMULA</div>
    <div class="rule" style="top:529px"></div>

    <p class="footnote" style="top:539px">*AVOID EYES/FOREHEAD BEFORE SWEATING AND SCRUFF (SNAGS FIBERS)</p>
    <div class="rule" style="top:582px"></div>

    <p class="centered care" style="top:591px">Please care for our planet, cities,<br>and sewer systems by recycling<br>this packaging after use.<br><strong>Do not flush packaging.</strong></p>

    <div class="size-box">10CM<br><span class="times">X</span><br>12CM</div>
    <p class="free-list">FRAGRANCES <span class="accent">FREE</span><br>PARABENS <span class="accent">FREE</span></p>
  </div>
</section>

</body>
</html>
```